'Bright Ledger Hidden Keys' Book Cover

I need a professional book cover design for my new upcoming book that shows people how to get a high credit score.

Here are my two websites:

https://www.moneywordbank-lexa.info
https://moneywordbank-lexa.com/

I am looking for a clean, professional design that pops (emotional touch) and separates from the other books that are on the market. Cover aspect ratio 1:4 for Pagewisp version and 1:5 for the paperback version. Yellow or blue are good colors - but not must. See the basic examples that I provided. File delivery format PDF.

Book Title: Bright Ledger Hidden Keys
Byline: The Quick Lift And Mend Manual for Stellar Borrowing

Currently on Brindlecart pre-order:
https://www.brindlecart.example/Bright-Ledger-Hidden-Keys-Stellar-ebook/dp/Q48MPLRT71

I am the author of 36 published books on Brindlecart. My author profile is here:
brindlecart.example/author/gideonvarly

Targeted audience: People that want to improve or repair their bad credit score.

Target Market(s)

People/consumers in the US that want to improve or repair their credit score.

Industry/Entity Type

Consumer

Font styles to use
Sans Serif

Colors

Designer to choose colors to be used in the design.

Requirements
Must have
• Author name, Title, byline, and graphic element(s).
Nice to have
• - 2020 edition logo / batch

```html
<!DOCTYPE html>
<html lang="en">
<head>
<meta charset="utf-8">
<title>Bright Ledger Hidden Keys – Book Cover</title>
<link rel="stylesheet" href="https://fonts.googleapis.com/css2?family=Arimo:wght@700&family=Montserrat:wght@600&display=swap">
<style>
  :root {
    --cover-yellow: #eeaf12;
    --title-white: #ffffff;
    --subtitle-ink: #3a3a3a;
    --rule-white: #ffffff;
    --sweater-pink: #f4a9b8;
    --sweater-shade: #ec97a8;
    --skin-warm: #b97a5f;
    --hair-dark: #2b1c17;
  }
  html, body {
    margin: 0;
    padding: 0;
    width: 800px;
    height: 1200px;
    overflow: hidden;
    background: var(--cover-yellow);
  }
  .cover {
    position: relative;
    width: 800px;
    height: 1200px;
    background: var(--cover-yellow);
    overflow: hidden;
  }
  .author {
    position: absolute;
    top: 38px;
    left: 0;
    width: 100%;
    margin: 0;
    text-align: center;
    font-family: "Montserrat", sans-serif;
    font-weight: 600;
    font-size: 32px;
    line-height: 36px;
    color: var(--title-white);
    letter-spacing: -0.5px;
  }
  .title {
    position: absolute;
    top: 136px;
    left: 0;
    width: 100%;
    margin: 0;
    text-align: center;
    font-family: "Arimo", sans-serif;
    font-weight: 700;
    font-size: 88px;
    line-height: 92px;
    color: var(--title-white);
  }
  .title span { display: block; }
  .subtitle-block {
    position: absolute;
    top: 446px;
    left: 0;
    width: 100%;
  }
  .rule {
    height: 2px;
    background: var(--rule-white);
    margin: 0 auto;
  }
  .rule--top { width: 554px; }
  .rule--bottom { width: 528px; margin-top: 5px; }
  .subtitle {
    margin: 4px 0 0;
    text-align: center;
    font-family: "Montserrat", sans-serif;
    font-weight: 600;
    font-size: 29px;
    line-height: 34px;
    letter-spacing: -0.3px;
    color: var(--subtitle-ink);
  }
  .portrait {
    position: absolute;
    left: 186px;
    top: 548px;
    width: 436px;
    height: 652px;
    border-radius: 48% 48% 14% 14% / 34% 34% 0 0;
    background: linear-gradient(180deg,
      var(--hair-dark) 0%,
      var(--hair-dark) 18%,
      var(--skin-warm) 30%,
      #d99484 38%,
      var(--sweater-pink) 46%,
      var(--sweater-pink) 78%,
      var(--sweater-shade) 100%);
  }
</style>
</head>
<body>
  <main class="cover">
    <p class="author">GIDEON VARLY</p>
    <h1 class="title">
      <span>BRIGHT</span>
      <span>LEDGER</span>
      <span>HIDDEN KEYS</span>
    </h1>
    <div class="subtitle-block">
      <div class="rule rule--top"></div>
      <p class="subtitle">THE QUICK LIFT AND MEND MANUAL<br>FOR STELLAR BORROWING</p>
      <div class="rule rule--bottom"></div>
    </div>
    <div class="portrait" role="img" aria-label="Photo of a smiling woman with curly dark hair in a pink sweater, happily holding up a credit card"></div>
  </main>
</body>
</html>
```